We need (2) 4"X4" product label designs for the front and back of an RTU hose on bottle (see attached examples) for a brand new, first-of-its-kind, Aloe Vera product (VerdaKin "The Supreme Root Tonic") specially formulated for agriculture. Most people are aware of the medicinal benefits of aloe vera, however, most people are unaware that it can be used as a soil amendment (organic fertilizer) for plants and lawns, as well as many other crops. This product is for the consumer market. There are about 15 elements that need to go on the front label (which I will provide moving forward), and the backside provides instructions and other relevant information about the product. I will provide a range of examples on the next step of this project.

Need extra days to review

```html
<!DOCTYPE html>
<html lang="en">
<head>
<meta charset="utf-8">
<title>VerdaKin – The Supreme Root Tonic label</title>
<link href="https://fonts.googleapis.com/css2?family=Domine:wght@700&family=Arimo:wght@400;700&family=Open+Sans:wght@300;400&display=swap" rel="stylesheet">
<style>
  :root{
    --page:#ffffff;
    --cream:#f6e4c8;
    --orange:#e08a0c;
    --orange-text:#e38b12;
    --ink:#111111;
    --cream-text:#fbecd6;
    --leaf:#0f5c2a;
    --sky-top:#e2742a;
    --sky-sun:#f6c640;
    --field-top:#6aa23a;
    --field-bottom:#2f6d1e;
    --aloe-light:#a8dc7a;
    --aloe-dark:#4f9a2c;
  }
  *{margin:0;padding:0;box-sizing:border-box}
  html,body{width:1200px;height:1200px;overflow:hidden;background:var(--page)}
  .label{position:absolute;left:100px;top:100px;width:1000px;height:1000px;background:var(--cream);overflow:hidden;font-family:"Arimo",Arial,sans-serif}
  .field-scene{position:absolute;left:0;top:0;width:1000px;height:325px;
    background:linear-gradient(180deg,var(--sky-top) 0%,var(--sky-sun) 12%,#d7a23a 17%,var(--field-top) 20%,#4e8a2a 60%,var(--field-bottom) 100%)}
  .aloe-art{position:absolute;left:680px;top:410px;width:320px;height:570px;
    background:radial-gradient(ellipse at 55% 70%,var(--aloe-light) 0%,var(--aloe-dark) 70%,rgba(79,154,44,0) 100%);border-radius:50% 50% 40% 40%}
  .title-panel{position:absolute;left:85px;top:154px;width:830px;height:530px;background:var(--orange);border-radius:24px;text-align:center}
  .brand{position:absolute;left:0;right:0;top:40px;font-family:"Domine",Georgia,serif;font-weight:700;font-size:116px;line-height:1;color:var(--ink)}
  .tagline-light{position:absolute;left:0;right:0;top:190px;font-family:"Open Sans",Arial,sans-serif;font-weight:300;font-size:72px;line-height:1;color:var(--cream-text)}
  .tagline-bold{position:absolute;left:0;right:0;top:278px;font-weight:700;font-size:80px;line-height:1;color:var(--cream-text)}
  .claim{position:absolute;left:0;right:0;top:393px;font-size:41px;color:var(--ink)}
  .subclaim{position:absolute;left:0;right:0;top:452px;font-size:33px;color:var(--cream-text)}
  .elements-title{position:absolute;left:85px;top:713px;font-weight:700;font-size:46px;color:var(--orange-text)}
  .elements-list{position:absolute;left:85px;top:778px;font-family:"Open Sans",Arial,sans-serif;font-size:31px;line-height:38px;letter-spacing:2px;color:var(--leaf);white-space:pre}
  .rule-h{position:absolute;left:85px;top:866px;width:505px;height:2px;background:var(--ink)}
  .rule-v{position:absolute;left:338px;top:872px;width:2px;height:86px;background:var(--ink)}
  .category{position:absolute;left:85px;top:884px;font-family:"Domine",Georgia,serif;font-weight:700;font-size:27px;line-height:32px;color:var(--ink)}
  .net-weight{position:absolute;left:372px;top:890px;font-family:"Domine",Georgia,serif;font-weight:700;font-size:34px;color:var(--ink)}
  .base-band{position:absolute;left:0;top:978px;width:1000px;height:22px;background:var(--orange)}
</style>
</head>
<body>
<main class="label">
  <div class="field-scene" role="img" aria-label="Photo of green crop fields under a sunset sky"></div>
  <div class="aloe-art" role="img" aria-label="Photo of aloe vera leaves and cut aloe slices"></div>
  <section class="title-panel">
    <h1 class="brand">VerdaKin</h1>
    <p class="tagline-light">THE SUPREME</p>
    <p class="tagline-bold">ROOT TONIC</p>
    <p class="claim">First-of-its-kind&nbsp; Aloe Vera product</p>
    <p class="subclaim">Specially formulated for agriculture</p>
  </section>
  <h2 class="elements-title">Include 15 Elements</h2>
  <p class="elements-list">XY  WT  UV  GX  GA  GE  QW  GB
HA  AW  BE  EW  BE  EW  BE</p>
  <div class="rule-h"></div>
  <div class="rule-v"></div>
  <p class="category">ORGANIC<br>FERTILIZER</p>
  <p class="net-weight">Net Wt.3L</p>
  <div class="base-band"></div>
</main>
</body>
</html>
```